Creative Businesss Card desgin!

Create a business card for our business Gleam window cleaning!
We are open to creative ideas as long as it maintains a professional image.

Target Market(s)

Small Commercial window cleaning clients including car dealerships, strata manager, cafe

Industry/Entity Type

Window Cleaning

Contact Information for Business Card

Daniel Prescott
General Manager
Gleam Window Cleaning

daniel@gleamservices.com.au
pane-care-southbank.com.au
Ph: 1800 GET GLEAM
Mob: 0437 582 061

Colors
fbed22
0392cd

Requirements
Should not have
• Stock window cleaning/ squeegee graphics

```html
<!DOCTYPE html>
<html lang="en">
<head>
<meta charset="utf-8">
<title>Gleam Window Cleaning – Business Card</title>
<link href="https://fonts.googleapis.com/css2?family=Arimo:wght@700&family=Roboto:wght@400;500&family=Roboto+Condensed:wght@500&display=swap" rel="stylesheet">
<style>
  :root {
    --backdrop: #2b2b2d;
    --card-blue: #0e5784;
    --gleam-yellow: #f2ec22;
    --text-white: #f2f4f6;
  }
  * { margin: 0; padding: 0; box-sizing: border-box; }
  html, body { width: 1200px; height: 960px; overflow: hidden; }
  body { background: var(--backdrop); position: relative; font-family: "Roboto", Arial, sans-serif; }

  .card {
    position: absolute;
    width: 598px; height: 342px;
    background: var(--card-blue);
  }
  .card--front { left: 322px; top: 108px; }
  .card--back { left: 320px; top: 493px; }

  .wordmark { position: absolute; color: var(--gleam-yellow); font-family: "Arimo", Arial, sans-serif; font-weight: 700; line-height: 1; }
  .wordmark__name { display: block; }
  .wordmark__line { display: block; }

  .card--front .wordmark { left: 31px; top: 30px; }
  .card--front .wordmark__name { font-size: 71px; letter-spacing: 1px; }
  .card--front .wordmark__line { font-size: 21px; margin-top: 6px; }

  .card--back .wordmark { left: 0; width: 100%; top: 110px; text-align: center; }
  .card--back .wordmark__name { font-size: 86px; letter-spacing: 2px; }
  .card--back .wordmark__line { font-size: 29px; margin-top: 12px; }

  .person { position: absolute; left: 31px; top: 159px; }
  .person__name { font-family: "Roboto Condensed", Arial, sans-serif; font-weight: 500; font-size: 23px; color: var(--gleam-yellow); line-height: 1; }
  .person__role { font-weight: 500; font-size: 14.5px; color: var(--text-white); margin-top: 5px; letter-spacing: 0.3px; }
  .company { position: absolute; left: 31px; top: 215px; font-size: 15px; color: var(--text-white); }

  .contacts { position: absolute; left: 31px; top: 242px; list-style: none; }
  .contacts li { display: flex; align-items: center; height: 19.3px; font-size: 14.8px; color: var(--text-white); }
  .contacts svg { width: 14px; height: 14px; margin-right: 8px; fill: var(--gleam-yellow); flex: none; }

  .card__url { position: absolute; left: 0; width: 100%; top: 287px; text-align: center; font-size: 15px; letter-spacing: 1.6px; color: var(--text-white); }
</style>
</head>
<body>
  <section class="card card--front">
    <div class="wordmark">
      <span class="wordmark__name">GLEAM</span>
      <span class="wordmark__line">WINDOW CLEANING</span>
    </div>
    <div class="person">
      <p class="person__name">DANIEL PRESCOTT</p>
      <p class="person__role">GENERAL MANAGER</p>
    </div>
    <p class="company">Gleam Window Cleaning</p>
    <ul class="contacts">
      <li><svg viewBox="0 0 16 16" aria-hidden="true"><path d="M3.6 1.2 6 3.6c.4.4.4 1 0 1.4L4.9 6.1c.9 1.9 3.1 4.1 5 5l1.1-1.1c.4-.4 1-.4 1.4 0l2.4 2.4c.4.4.4 1 0 1.4l-1.3 1.3C11.7 16.9 1.1 6.3 2.9 4.5L3.6 1.2z"/></svg>1800 GET GLEAM</li>
      <li><svg viewBox="0 0 16 16" aria-hidden="true"><path d="M4.5 0h7A1.5 1.5 0 0 1 13 1.5v13a1.5 1.5 0 0 1-1.5 1.5h-7A1.5 1.5 0 0 1 3 14.5v-13A1.5 1.5 0 0 1 4.5 0zM5 2v10h6V2H5zm3 11a1 1 0 1 0 0 2 1 1 0 0 0 0-2z"/></svg>0437 582 061</li>
      <li><svg viewBox="0 0 16 16" aria-hidden="true"><path d="M1 4h14v1L8 9.5 1 5V4zm0 2.6 7 4.5 7-4.5V13H1V6.6z"/></svg>daniel@gleamservices.com.au</li>
      <li><svg viewBox="0 0 16 16" aria-hidden="true"><path d="M8 1a7 7 0 1 0 0 14A7 7 0 0 0 8 1zm0 1.5c.6 0 1.4 1.2 1.8 3.5H6.2C6.6 3.7 7.4 2.5 8 2.5zM2.6 7.5h2.5a11 11 0 0 0 0 1H2.6a5.6 5.6 0 0 1 0-1zm3.5 0h3.8a10 10 0 0 1 0 1H6.1a10 10 0 0 1 0-1zm4.8 0h2.5a5.6 5.6 0 0 1 0 1h-2.5a11 11 0 0 0 0-1zM6.2 10h3.6c-.4 2.3-1.2 3.5-1.8 3.5S6.6 12.3 6.2 10z"/></svg>pane-care-southbank.com.au</li>
    </ul>
  </section>

  <section class="card card--back">
    <div class="wordmark">
      <span class="wordmark__name">GLEAM</span>
      <span class="wordmark__line">WINDOW CLEANING</span>
    </div>
    <p class="card__url">www.pane-care-southbank.com.au</p>
  </section>
</body>
</html>
```